Medical Implant company needs a Top Quality Premium Brochure

We need to create a top quality brochure for VIP clients, formed by top spine surgeons. The main goal here is to cause a deep quality impact, positioning the company and it´s solutions above the others, with a refined, unique and creative material.

Special paper, hot stamping, innovative format are welcome.

For more information check out our website: www.veltrosan.com.br (web translator are recommended for content understanding)

Veltrosan works with top quality spine and pain management products, providing solutions for the medical specialists, investing in high quality processes and continued medical education.

Short briefing:
1 - Company profile
2 - Quality / vision
3 - Continued education programs
4 - Main products
5 - Main partners
6 - Final stuff (creative final thoughts / considerations)

FORMAT: 25 x 18,5 cm (horizontal)
PAGES - 16

REFERENCES:

https://www.folivenk.net/gallery/52917340/Medical-Healthcare-Profile-Brochure

https://www.folivenk.net/gallery/7810263/TK-Alpine-Style-Brochure

Target Market(s)

Mainly brazilian spine and neuro surgeons with minimally invasive surgery skills.

Industry/Entity Type

Education

Requirements
Must have

• 18 pages design

1. Cover
2. IMAGE + TITLE - About Us
3. IMAGE + TEXT - About Us
4. IMAGE + TITLE - Vision
5. IMAGE + TEXT - Vision
6. IMAGE + TITLE - Quality
7. IMAGE + TEXT - Quality
8. Timeline Left
9. Timeline Right
10. IMAGE + TITLE - Medical Education
11. IMAGE + TEXT - Medical Education
12. IMAGE + TITLE - Minimally Invasive Technology
13. IMAGE + TEXT - Minimally Invasive Technology
14. IMAGE + TITLE - Impact Phrase
15. IMAGE + TEXT - Impact Phrase
16. Back

As longs as the text is under development and will be placed internally in the winning design, please use 'lorem ipsum' for text areas. The titles can follow the index above.

Nice to have
• The use of office pictures with some style / artistic finish in pages "about us"

```html
<!DOCTYPE html>
<html lang="en">
<head>
<meta charset="utf-8">
<title>Veltrosan Brochure</title>
<link href="https://fonts.googleapis.com/css2?family=Barlow:wght@300;400;600&display=swap" rel="stylesheet">
<style>
:root{
  --bg:#e3e3e3;
  --paper:#ffffff;
  --green:#3a9a5b;
  --ink:#4a4a4a;
  --muted:#9a9a9a;
  --rule:#bdbdbd;
}
*{box-sizing:border-box;margin:0;padding:0}
html,body{width:1200px;height:3495px;overflow:hidden}
body{background:var(--bg);font-family:"Barlow",sans-serif;color:var(--ink);position:relative}
.cover{position:absolute;left:250px;top:160px;width:700px;height:518px;background:var(--paper);box-shadow:0 2px 6px rgba(0,0,0,.08)}
.cover-band{position:absolute;left:40px;top:40px;width:150px;height:300px;background:linear-gradient(160deg,#ececec,#f8f8f8 70%);opacity:.9}
.cover-brand{position:absolute;left:340px;top:220px;text-align:left}
.brand-name{font-size:30px;font-weight:600;color:var(--green);letter-spacing:.5px;display:flex;align-items:center;gap:8px}
.brand-mark{width:10px;height:10px;background:var(--green)}
.brand-tag{font-size:9px;color:var(--muted);margin-top:2px;letter-spacing:1px;padding-left:18px}
.spread{position:absolute;left:60px;width:1080px;height:400px;display:flex;box-shadow:0 2px 6px rgba(0,0,0,.08)}
.page{position:relative;width:540px;height:400px;background:var(--paper)}
.page.left{background:linear-gradient(90deg,#fff 92%,#f0f0f0)}
.page.right{background:linear-gradient(90deg,#f0f0f0,#fff 8%)}
.photo{position:absolute}
.title{position:absolute;font-weight:300;font-size:22px;line-height:1.05;text-transform:uppercase;letter-spacing:1px;color:var(--ink)}
.title .accent{color:var(--green)}
.body{position:absolute;font-size:6.5px;line-height:1.5;color:var(--muted)}
.col-head{font-size:7px;font-weight:600;color:var(--ink);text-transform:uppercase;margin-bottom:3px}
.foot-rule{position:absolute;left:40px;right:40px;bottom:28px;height:1px;background:var(--rule)}
.timeline{position:absolute;left:0;top:0}
.year{position:absolute;color:var(--green);font-weight:400;font-size:20px}
.year.small{font-size:10px;color:var(--muted)}
.founded{position:absolute;left:40px;top:206px;font-size:11px;text-transform:uppercase;line-height:1.15;color:var(--ink)}
.founded .year{position:static;display:block;font-size:24px}
.event{position:absolute;width:90px;font-size:6px;line-height:1.5;color:var(--muted)}
.edu-block{position:absolute;width:130px}
.edu-block .col-head{display:flex;align-items:center;gap:4px}
.edu-block .col-head::before{content:"";width:5px;height:5px;background:var(--green)}
</style>
</head>
<body>

<section class="cover">
  <div class="cover-band" role="img" aria-label="Faint decorative stripe motif"></div>
  <div class="cover-brand">
    <div class="brand-name"><span class="brand-mark"></span>Veltrosan</div>
    <div class="brand-tag">spine and pain solutions</div>
  </div>
</section>

<section class="spread" style="top:995px">
  <div class="page left">
    <div class="photo" style="left:40px;top:40px;width:160px;height:160px;background:linear-gradient(135deg,#7fc2bd,#3f8f93)" role="img" aria-label="Surgeons in scrubs during an operation"></div>
    <div class="photo" style="left:208px;top:40px;width:292px;height:160px;background:linear-gradient(135deg,#cfcfcf,#8d8d8d)" role="img" aria-label="Company name on the office wall"></div>
    <div class="photo" style="left:40px;top:208px;width:160px;height:140px;background:linear-gradient(135deg,#d9d3c8,#8a857c)" role="img" aria-label="Spinal implant instruments"></div>
    <div class="photo" style="left:208px;top:208px;width:292px;height:140px;background:linear-gradient(135deg,#b8b8b8,#4e4e4e)" role="img" aria-label="Modern office meeting room"></div>
  </div>
  <div class="page right">
    <h2 class="title" style="left:40px;top:50px">About <span class="accent">Us</span></h2>
    <p class="body" style="left:175px;top:170px;width:150px">Lorem ipsum dolor sit amet, consectetur adipiscing elit, sed do eiusmod tempor incididunt ut labore et dolore magna aliqua. Ut enim ad minim veniam, quis nostrud exercitation ullamco laboris.</p>
    <p class="body" style="left:345px;top:110px;width:150px">Lorem ipsum dolor sit amet, consectetur adipiscing elit, sed do eiusmod tempor incididunt ut labore et dolore magna aliqua. Ut enim ad minim veniam, quis nostrud exercitation ullamco laboris.</p>
  </div>
</section>

<section class="spread" style="top:1652px">
  <div class="page left">
    <h2 class="title" style="left:40px;top:150px">About<br><span class="accent">Veltrosan</span></h2>
    <p class="body" style="left:195px;top:145px;width:300px">Lorem ipsum dolor sit amet, consectetur adipiscing elit, sed do eiusmod tempor incididunt ut labore et dolore magna aliqua. Ut enim ad minim veniam, quis nostrud exercitation ullamco laboris.</p>
    <div class="body" style="left:195px;top:200px;width:95px"><div class="col-head">History</div>Duis aute irure dolor in reprehenderit in voluptate velit esse cillum dolore eu fugiat nulla pariatur.</div>
    <div class="body" style="left:305px;top:200px;width:95px"><div class="col-head">Vision</div>Duis aute irure dolor in reprehenderit in voluptate velit esse cillum dolore eu fugiat nulla pariatur.</div>
    <div class="body" style="left:415px;top:200px;width:95px"><div class="col-head">Quality</div>Duis aute irure dolor in reprehenderit in voluptate velit esse cillum dolore eu fugiat nulla pariatur.</div>
    <div class="foot-rule"></div>
  </div>
  <div class="page right">
    <div class="photo" style="left:20px;top:20px;width:520px;height:340px;background:radial-gradient(circle at 40% 55%,#8a6d9a,#2c2436 55%,#0d0c12)" role="img" aria-label="Glowing neuron network"></div>
  </div>
</section>

<section class="spread" style="top:2298px">
  <div class="page left"></div>
  <div class="page right"></div>
  <svg class="timeline" width="1080" height="400" viewBox="0 0 1080 400">
    <g stroke="#bdbdbd" stroke-width="1">
      <line x1="40" y1="200" x2="1040" y2="200"/>
      <line x1="170" y1="70" x2="170" y2="330"/>
      <line x1="380" y1="120" x2="380" y2="300"/>
      <line x1="700" y1="50" x2="700" y2="280"/>
      <line x1="950" y1="60" x2="950" y2="320"/>
    </g>
    <g fill="#3a9a5b">
      <circle cx="170" cy="200" r="3"/><circle cx="380" cy="200" r="3"/>
      <circle cx="700" cy="200" r="3"/><circle cx="950" cy="200" r="3"/>
    </g>
  </svg>
  <div class="founded"><span class="year">2002</span>Veltrosan<br>was<br>established</div>
  <div class="year" style="left:150px;top:335px">2007</div>
  <div class="year small" style="left:367px;top:305px">2009</div>
  <div class="year" style="left:680px;top:22px">2012</div>
  <div class="year small" style="left:687px;top:285px">2013</div>
  <div class="year" style="left:965px;top:48px">2015</div>
  <p class="event" style="left:180px;top:75px">Lorem ipsum dolor sit amet, consectetur adipiscing elit.</p>
  <div class="photo" style="left:240px;top:145px;width:40px;height:30px;background:linear-gradient(135deg,#e2c9a6,#7d9b8a)" role="img" aria-label="Training session"></div>
  <div class="photo" style="left:125px;top:240px;width:35px;height:35px;background:linear-gradient(135deg,#9aa6b0,#3c4650)" role="img" aria-label="Spine x-ray"></div>
  <p class="event" style="left:390px;top:125px">Lorem ipsum dolor sit amet, consectetur adipiscing elit.</p>
  <div class="photo" style="left:620px;top:215px;width:60px;height:40px;background:linear-gradient(135deg,#bfd2de,#5f7f93)" role="img" aria-label="Surgeon at work"></div>
  <p class="event" style="left:710px;top:110px">Lorem ipsum dolor sit amet, consectetur adipiscing elit.</p>
  <p class="event" style="left:710px;top:220px">Lorem ipsum dolor sit amet, consectetur adipiscing elit.</p>
  <div class="photo" style="left:850px;top:55px;width:40px;height:35px;background:linear-gradient(135deg,#cfcfcf,#2a2a2a)" role="img" aria-label="Surgical instrument"></div>
  <p class="event" style="left:960px;top:85px;width:75px">Lorem ipsum dolor sit amet, consectetur adipiscing elit.</p>
</section>

<section class="spread" style="top:2963px">
  <div class="page left">
    <h2 class="title" style="left:40px;top:60px">Medical<br><span class="accent">Education</span></h2>
    <div class="edu-block body" style="left:40px;top:220px"><div class="col-head">Headline</div>Lorem ipsum dolor sit amet, consectetur adipiscing elit.</div>
    <div class="edu-block body" style="left:190px;top:220px"><div class="col-head">Headline</div>Lorem ipsum dolor sit amet, consectetur adipiscing elit.</div>
    <div class="edu-block body" style="left:340px;top:220px"><div class="col-head">Headline</div>Lorem ipsum dolor sit amet, consectetur adipiscing elit.</div>
    <div class="edu-block body" style="left:40px;top:300px"><div class="col-head">Headline</div>Lorem ipsum dolor sit amet, consectetur adipiscing elit.</div>
    <div class="edu-block body" style="left:190px;top:300px"><div class="col-head">Headline</div>Lorem ipsum dolor sit amet, consectetur adipiscing elit.</div>
    <div class="edu-block body" style="left:340px;top:300px"><div class="col-head">Headline</div>Lorem ipsum dolor sit amet, consectetur adipiscing elit.</div>
  </div>
  <div class="page right">
    <div class="photo" style="left:20px;top:20px;width:240px;height:170px;background:linear-gradient(135deg,#6fbfb4,#2f7f86)" role="img" aria-label="Medical team in teal scrubs"></div>
    <div class="photo" style="left:268px;top:20px;width:252px;height:120px;background:linear-gradient(135deg,#eef2f5,#8fa3b3)" role="img" aria-label="Doctor at a microscope"></div>
    <div class="photo" style="left:268px;top:148px;width:252px;height:100px;background:linear-gradient(135deg,#c7d6df,#6a8797)" role="img" aria-label="Surgical workshop"></div>
    <div class="photo" style="left:20px;top:198px;width:150px;height:162px;background:linear-gradient(135deg,#e8e8e8,#9aa5ac)" role="img" aria-label="Students in a lab"></div>
    <div class="photo" style="left:178px;top:198px;width:82px;height:162px;background:linear-gradient(135deg,#c9c9c9,#5a5a5a)" role="img" aria-label="Instrument tray"></div>
    <div class="photo" style="left:268px;top:256px;width:252px;height:104px;background:linear-gradient(135deg,#5fae9f,#1f5d62)" role="img" aria-label="Surgery in progress"></div>
  </div>
</section>

</body>
</html>
```